The Quiet Hour Safeguard Handbook

A book cover. The book will be marketed as a promotional item for financial advisors, financial planners, independent insurance agents, bankers, and any professional who views their role as guardian of their clients assets and helping them manage risk.

```html
<!DOCTYPE html>
<html lang="en">
<head>
<meta charset="UTF-8">
<title>The Quiet Hour Safeguard Handbook — Cover</title>
<link href="https://fonts.googleapis.com/css2?family=Bebas+Neue&family=Outfit:wght@300;500&display=swap" rel="stylesheet">
<style>
  :root {
    --backdrop: #e9e8e5;
    --navy: #0f2a55;
    --navy-deep: #0b2249;
    --white: #ffffff;
    --gold: #b8903f;
  }
  * { margin: 0; padding: 0; box-sizing: border-box; }
  html, body {
    width: 1000px;
    height: 1200px;
    overflow: hidden;
    background: var(--backdrop);
  }
  .cover {
    position: absolute;
    left: 100px;
    top: 20px;
    width: 800px;
    height: 1160px;
    background: linear-gradient(180deg, var(--navy) 0%, var(--navy-deep) 100%);
    color: var(--white);
    text-align: center;
  }
  .title-lead,
  .title-main {
    position: absolute;
    left: 0;
    width: 100%;
    font-family: "Bebas Neue", "Oswald", sans-serif;
    font-weight: 400;
    line-height: 1;
    letter-spacing: 3px;
    color: var(--white);
  }
  .title-lead {
    top: 80px;
    font-size: 190px;
  }
  .title-main {
    top: 250px;
    font-size: 176px;
  }
  .inner-title-frame {
    position: absolute;
    left: 190px;
    top: 470px;
    width: 420px;
    height: 420px;
    border: 6px solid var(--gold);
    display: flex;
    align-items: center;
    justify-content: center;
  }
  .inner-title {
    font-family: "Bebas Neue", "Oswald", sans-serif;
    font-weight: 400;
    font-size: 88px;
    line-height: 1;
    letter-spacing: 2px;
    color: var(--white);
  }
  .subtitle {
    position: absolute;
    left: 0;
    top: 968px;
    width: 100%;
    font-family: "Outfit", "Helvetica Neue", sans-serif;
    font-weight: 500;
    font-size: 26px;
    color: var(--white);
  }
  .tagline {
    position: absolute;
    left: 0;
    top: 1050px;
    width: 100%;
    font-family: "Outfit", "Helvetica Neue", sans-serif;
    font-weight: 300;
    font-size: 19px;
    line-height: 1.6;
    color: var(--white);
  }
</style>
</head>
<body>
  <main class="cover">
    <h1>
      <span class="title-lead">The</span>
      <span class="title-main">Quiet Hour</span>
    </h1>

    <div class="inner-title-frame">
      <h2 class="inner-title">Safeguard<br>Handbook</h2>
    </div>

    <p class="subtitle">Protect Yourself And Your Family In Th Ai Age</p>
    <p class="tagline">it’s better to have it and not need it<br>than need it and not have it</p>
  </main>
</body>
</html>
```